Commercial photographer, UAV drone photography & 360 walk-through visuals

I need a business card design that is minimalist but yet pretentiously creative. My target market are architects, designers, advertising agents and marketing managers. It is important to stress that though I am asking for a minimalist design it needs to have creative impact.

Target Market(s)

Architects, interiors designers, web-designers, artists

Contact Information for Business Card

Include my name, mobile [cell] number, email, web page and the company logo. Do not to include a postal address.

Colors

Designer to choose colors to be used in the design.

Requirements
Must have
• The following information is to be included:
• Milo Fenwick
• Photographer
• m: 07812 593174
• e: milo@mfimagery.co.uk
• w: mfimagery.co.uk

```html
<!DOCTYPE html>
<html lang="en">
<head>
<meta charset="utf-8">
<title>MF Imagery – Business Card</title>
<link href="https://fonts.googleapis.com/css2?family=Lato:wght@300;400;700&display=swap" rel="stylesheet">
<style>
  :root {
    --backdrop: #3a3a3a;
    --card: #1c1c1c;
    --ink: #f2f2f2;
    --ink-soft: #d6d6d6;
    --mark-tone: #8c8c8c;
    --rule: #9a9a9a;
  }
  * { margin: 0; padding: 0; box-sizing: border-box; }
  html, body {
    width: 1200px; height: 900px; overflow: hidden;
    background: var(--backdrop);
    font-family: "Lato", sans-serif;
  }
  .canvas {
    width: 1200px; height: 900px;
    display: flex; flex-direction: column;
    align-items: center; justify-content: center; gap: 60px;
  }
  .card {
    width: 600px; height: 345px;
    background: var(--card);
    position: relative;
  }
  /* Front side */
  .card--front {
    display: flex; flex-direction: column;
    align-items: center; justify-content: center;
  }
  .brand {
    display: flex; align-items: center; gap: 14px;
  }
  .brand__dot {
    width: 14px; height: 14px; border-radius: 50%;
  }
  .brand__name {
    font-weight: 300; letter-spacing: 6px; text-transform: uppercase;
  }
  .card--front .brand__dot { background: var(--mark-tone); }
  .card--front .brand__name { color: var(--mark-tone); font-size: 46px; }
  .card--front .site {
    margin-top: 38px; color: var(--ink-soft);
    font-size: 15px; letter-spacing: 0.5px;
  }
  /* Back side */
  .card--back {
    display: flex; align-items: center;
    padding: 0 44px;
  }
  .card--back .brand { width: 240px; }
  .card--back .brand__dot { background: var(--ink); width: 10px; height: 10px; }
  .card--back .brand__name { color: var(--ink); font-size: 26px; letter-spacing: 4px; }
  .divider {
    width: 1px; height: 130px; background: var(--rule);
    margin: 0 34px 0 10px;
  }
  .contact { color: var(--ink); }
  .contact__name { font-weight: 700; font-size: 22px; }
  .contact__role { font-size: 15px; color: var(--ink-soft); margin: 2px 0 12px; }
  .contact__list { list-style: none; }
  .contact__item {
    display: flex; align-items: center; gap: 10px;
    font-size: 15px; line-height: 22px;
  }
  .contact__icon { width: 13px; height: 13px; flex: none; }
  .contact__icon--blank { visibility: hidden; }
</style>
</head>
<body>
<main class="canvas">
  <section class="card card--front" aria-label="Card front">
    <div class="brand">
      <span class="brand__dot"></span>
      <span class="brand__name">MF Imagery</span>
    </div>
    <p class="site">www.mfimagery.co.uk</p>
  </section>

  <section class="card card--back" aria-label="Card back">
    <div class="brand">
      <span class="brand__dot"></span>
      <span class="brand__name">MF Imagery</span>
    </div>
    <span class="divider"></span>
    <div class="contact">
      <p class="contact__name">Milo Fenwick</p>
      <p class="contact__role">Commercial Photographer</p>
      <ul class="contact__list">
        <li class="contact__item">
          <svg class="contact__icon" viewBox="0 0 14 14" aria-hidden="true"><rect x="3.5" y="0.8" width="7" height="12.4" rx="1.2" fill="none" stroke="#f2f2f2" stroke-width="1.2"/><line x1="6" y1="11" x2="8" y2="11" stroke="#f2f2f2" stroke-width="1.2"/></svg>
          07812 593174
        </li>
        <li class="contact__item">
          <svg class="contact__icon" viewBox="0 0 14 14" aria-hidden="true"><rect x="0.8" y="2.5" width="12.4" height="9" fill="#f2f2f2"/><polyline points="0.8,2.5 7,8 13.2,2.5" fill="none" stroke="#1c1c1c" stroke-width="1.2"/></svg>
          milo@mfimagery.co.uk
        </li>
        <li class="contact__item">
          <svg class="contact__icon" viewBox="0 0 14 14" aria-hidden="true"><circle cx="7" cy="7" r="6.2" fill="#f2f2f2"/><ellipse cx="7" cy="7" rx="2.6" ry="6.2" fill="none" stroke="#1c1c1c" stroke-width="1"/><line x1="0.8" y1="7" x2="13.2" y2="7" stroke="#1c1c1c" stroke-width="1"/></svg>
          www.mfimagery.co.uk
        </li>
      </ul>
    </div>
  </section>
</main>
</body>
</html>
```